Real Estate Investor needs awesome business card design

I invest in real estate, focused on multi-family properties, and I need a business card to hand out to potential partners. I prefer simple, clean designs, but it needs to stand out, so I'd like there to be a bit of red in the design as well.

It should include this information:

Front
Dallin Pecksworth
Real Estate Investor
Direct phone: 502-867-3394
Email: dallinhpecksworth@quillmail.example
Headshot (Picture), I've uploaded a few, just pick the one you think looks best with your design. You can remove the background from the headshot image if it looks better.

Back
The back of the card's design should flow and be congruent with the front. On the back I want to put an inspirational quote or question. There will be different ones depending on the card, so I'll need the original file so I can edit it in the end.

For now, use “The Pessimist Sees Difficulty In Every Opportunity. The Optimist Sees The Opportunity In Every Difficulty.” -Barnaby Ellsworth

Target Market(s)

Investors

Industry/Entity Type

Real Estate

Contact Information for Business Card

Front
Dallin Pecksworth
Real Estate Investor

Back
The back of the card's design should flow and be congruent with the front. On the back I want to put an inspirational quote or question. There will be different ones depending on the card, so I'll need the original file so I can edit it in the end. I've uploaded some EXAMPLES of business cards with quotes on them. Don't copy but feel free to use them as inspiration.

The design will be printed on "ZIB sized" business cards
1039 x 697 pixels
with rounded corners

Font styles to use
Serif
Decorative
Script

Colors
ec1f27

Requirements
Must have
• Headshot, name, and other information in it.
• 1039 x 697 pixels
• Rounded corners
• Clean design that pops. I'm open to see any color background, including black.
• Headshots can be located here: https://www.filecrate.example/sh/8kd2wq7mzt31hvx/BBQTXP4ruf9LmQ0KhcvWx7b?dl=0
Nice to have
• It would be awesome if the design included a personal signature or monogram, but if not I'll get a personal logo developed later and the card redesigned if I think it needs it.
Should not have
• Cluttered design

```html
<!DOCTYPE html>
<html lang="en">
<head>
<meta charset="utf-8">
<title>Dallin Pecksworth – Business Card</title>
<link rel="stylesheet" href="https://fonts.googleapis.com/css2?family=Arvo:wght@400;700&family=Roboto+Slab:wght@300;400;900&display=swap">
<style>
  :root {
    --backdrop: #3b3b3b;
    --card-white: #ffffff;
    --brand-red: #ec1f27;
    --brand-plum: #a11b60;
    --accent-yellow: #ffed00;
    --ink: #2b2b2b;
    --photo-light: #ece9e6;
    --photo-skin: #d9a98c;
    --photo-suit: #1f2a44;
  }
  * { box-sizing: border-box; margin: 0; padding: 0; }
  html, body { width: 1200px; height: 1200px; overflow: hidden; }
  body { background: var(--backdrop); position: relative; }

  .card {
    position: absolute;
    width: 390px;
    height: 223px;
    border-radius: 12px;
    overflow: hidden;
  }
  .card--front { background: var(--card-white); top: 351px; }
  .card--back { top: 627px; }
  .card--left { left: 174px; }
  .card--right { left: 635px; }
  .theme-red { --accent: var(--brand-red); }
  .theme-plum { --accent: var(--brand-plum); }
  .card--back { background: var(--accent); }

  .quote-mark {
    position: absolute;
    font-family: "Roboto Slab", serif;
    font-weight: 900;
    font-size: 96px;
    line-height: 1;
    height: 48px;
    overflow: hidden;
  }
  .card--front .quote-mark { left: 27px; top: 22px; color: var(--accent); }
  .card--back .quote-mark--open { left: 23px; top: 18px; color: var(--accent-yellow); }
  .card--back .quote-mark--close { right: 20px; bottom: 22px; color: var(--accent-yellow); height: 46px; }

  .headshot {
    position: absolute;
    left: 145px; right: 0; top: 12px; bottom: 0;
    background: radial-gradient(ellipse 30% 42% at 68% 38%, var(--photo-skin) 0%, var(--photo-skin) 55%, transparent 75%),
                linear-gradient(to bottom, var(--card-white) 0%, var(--card-white) 62%, var(--photo-suit) 85%);
    opacity: 0.9;
    clip-path: polygon(30% 100%, 45% 70%, 50% 10%, 66% 0%, 82% 10%, 84% 65%, 100% 92%, 100% 100%);
  }

  .contact {
    position: absolute;
    left: 28px; top: 93px;
    font-family: "Roboto Slab", serif;
    font-weight: 300;
    color: var(--ink);
  }
  .contact__name {
    font-family: "Arvo", serif;
    font-weight: 400;
    font-size: 15px;
    color: var(--accent);
    letter-spacing: 0.2px;
  }
  .contact__title { font-size: 10px; margin-top: 1px; }
  .contact__lines { margin-top: 13px; font-size: 9.5px; line-height: 13px; }
  .contact__label { color: var(--accent); display: inline-block; width: 37px; }

  .quote {
    position: absolute;
    left: 0; width: 380px; top: 69px;
    text-align: center;
    font-family: "Arvo", serif;
    font-weight: 400;
    font-size: 14.5px;
    line-height: 18.5px;
    color: var(--card-white);
    letter-spacing: 0.2px;
  }
  .quote em { font-style: normal; color: var(--accent-yellow); }
  .quote__author {
    position: absolute;
    left: 0; width: 380px; top: 166px;
    text-align: center;
    font-family: "Roboto Slab", serif;
    font-weight: 300;
    font-size: 9.5px;
    color: var(--accent-yellow);
  }
</style>
</head>
<body>

  <section class="card card--front card--left theme-red">
    <div class="headshot" role="img" aria-label="Headshot of Dallin Pecksworth, background removed"></div>
    <div class="quote-mark">“</div>
    <div class="contact">
      <h1 class="contact__name">Dallin Pecksworth</h1>
      <p class="contact__title">Real Estate Investor</p>
      <p class="contact__lines"><span class="contact__label">phone</span>: 502-867-3394<br><span class="contact__label">Email</span>: dallinhpecksworth@quillmail.example</p>
    </div>
  </section>

  <section class="card card--front card--right theme-plum">
    <div class="headshot" role="img" aria-label="Headshot of Dallin Pecksworth, background removed"></div>
    <div class="quote-mark">“</div>
    <div class="contact">
      <h1 class="contact__name">Dallin Pecksworth</h1>
      <p class="contact__title">Real Estate Investor</p>
      <p class="contact__lines"><span class="contact__label">phone</span>: 502-867-3394<br><span class="contact__label">Email</span>: dallinhpecksworth@quillmail.example</p>
    </div>
  </section>

  <section class="card card--back card--left theme-red">
    <div class="quote-mark quote-mark--open">“</div>
    <p class="quote">The <em>Pessimist</em> Sees<br>Difficulty In Every Opportunity.<br>The <em>Optimist</em> Sees<br>The Opportunity In Every Difficulty.</p>
    <p class="quote__author">{ Barnaby Ellsworth }</p>
    <div class="quote-mark quote-mark--close">”</div>
  </section>

  <section class="card card--back card--right theme-plum">
    <div class="quote-mark quote-mark--open">“</div>
    <p class="quote">The <em>Pessimist</em> Sees<br>Difficulty In Every Opportunity.<br>The <em>Optimist</em> Sees<br>The Opportunity In Every Difficulty.</p>
    <p class="quote__author">{ Barnaby Ellsworth }</p>
    <div class="quote-mark quote-mark--close">”</div>
  </section>

</body>
</html>
```